Quillrests.com website overhaul

We want to upgrade our Wix website into a professional looking page for our growing business. The content that is online now needs to be used but the site should have a new look and feel from top to bottom. QuillRests is a company in the hospital and nursing home space. We would like to see the website use our color scheme but other than that we are open to any and all ideas. www.quillrests.com

```html
<!DOCTYPE html>
<html lang="en">
<head>
<meta charset="utf-8">
<title>QuillRests — Enhanced Protection Against Airborne Infectious Particles</title>
<link href="https://fonts.googleapis.com/css2?family=DM+Sans:wght@300;400;500;700&family=Montserrat:wght@300;400;500;700;800&display=swap" rel="stylesheet">
<style>
:root{
  --ink:#2a1d6b;
  --ink-deep:#24174f;
  --hero-a:#3b2d8e;
  --hero-b:#2a2270;
  --orange:#f1582c;
  --band:#4b57b1;
  --band-b:#3e4aa3;
  --lavender:#e9e9f5;
  --text:#3a3a4a;
  --white:#ffffff;
  --pale:#cfd3ec;
}
*{box-sizing:border-box;margin:0;padding:0}
html,body{width:1200px;height:3622px;overflow:hidden}
body{font-family:"DM Sans",sans-serif;color:var(--text);background:var(--white);position:relative}
.abs{position:absolute}
.brand{display:flex;align-items:center;gap:14px;font-family:"Montserrat",sans-serif;font-weight:700;font-size:36px;color:var(--ink)}
.brand-mark{width:34px;height:34px;background:var(--ink);border-radius:4px}
.nav{top:0;left:0;width:1200px;height:82px;background:var(--white)}
.nav .brand{position:absolute;left:108px;top:18px}
.nav-links{position:absolute;left:471px;top:30px;display:flex;gap:77px;font-family:"DM Sans",sans-serif;font-weight:500;font-size:15px;color:var(--ink)}
.nav-links .current{border-bottom:2px solid var(--ink);padding-bottom:4px}
.phone{display:flex;align-items:center;gap:9px;font-weight:700;font-size:15px;color:var(--ink)}
.phone-dot{width:28px;height:28px;border-radius:50%;background:var(--orange);display:flex;align-items:center;justify-content:center}
.nav .phone{position:absolute;left:944px;top:27px}
.hero{top:82px;left:0;width:1200px;height:653px;background:radial-gradient(ellipse at 70% 30%,var(--hero-a),var(--hero-b));overflow:hidden}
.hero-copy{left:107px;top:186px;color:var(--white)}
.hero-copy .kicker{font-family:"DM Sans",sans-serif;font-size:27px;font-weight:400}
.hero-copy h1{font-family:"Montserrat",sans-serif;font-weight:800;font-size:41px;line-height:49px;margin-top:6px}
.btn{display:inline-flex;align-items:center;justify-content:center;background:var(--orange);color:var(--white);font-family:"DM Sans",sans-serif;font-weight:500;font-size:15px}
.hero .btn{position:absolute;left:112px;top:389px;width:177px;height:50px}
.hero-video{left:577px;top:119px;width:568px;height:376px;border-radius:6px;background:linear-gradient(180deg,#2aa6d6 0%,#33a9d4 70%,#b5b7c6 70%,#a9abbd 100%)}
.play{left:828px;top:266px;width:66px;height:66px;border-radius:50%;background:var(--orange)}
.hero-curve{left:0;top:660px;width:1200px;height:80px}
.center{text-align:center;width:1200px;left:0}
.eyebrow{font-family:"DM Sans",sans-serif;font-size:19px;color:var(--ink)}
.section-title{font-family:"Montserrat",sans-serif;font-weight:300;color:var(--ink)}
.section-title b{font-weight:700}
.rule{width:56px;height:2px;background:var(--ink)}
.dots-deco{left:1030px;top:725px;width:170px;height:210px;background:radial-gradient(circle at 70% 30%,#eceef6,#ffffff 75%)}
.about-body{left:180px;top:897px;width:840px;font-size:19px;line-height:28px;text-align:center;color:#2f2f3f}
.about-body p+p{margin-top:16px}
.band{top:1202px;left:0;width:1200px;height:587px;background:linear-gradient(135deg,var(--band),var(--band-b))}
.band-copy{left:122px;top:1378px;color:var(--white)}
.band-copy h2{font-family:"Montserrat",sans-serif;font-weight:300;font-size:42px;line-height:54px}
.band-copy h2 b{font-weight:700}
.band-copy p{margin:14px 0 0 9px;font-size:22px;line-height:33px;font-weight:300}
.band-art{left:600px;top:1262px;width:424px;height:460px;border-radius:50%;background:radial-gradient(circle,#d6e8ef 0%,#c2dbe7 45%,rgba(75,87,177,0) 72%)}
.n95-art{left:122px;top:1856px;width:420px;height:470px;background:radial-gradient(ellipse at 40% 55%,#ffffff 30%,#e6e8f4 55%,#ffffff 80%)}
.split-copy{left:597px;width:480px}
.split-copy h2{font-family:"Montserrat",sans-serif;font-weight:400;font-size:36px;line-height:47px;color:var(--ink)}
.split-copy h2 b{font-weight:700}
.n95 p{margin-top:30px;font-size:14px;line-height:24.6px;color:#3a3a4a}
.features{top:2395px;left:0;width:1200px;height:500px;background:var(--lavender)}
.card{top:2513px;width:454px;height:277px;background:var(--white);text-align:center}
.card h3{font-family:"Montserrat",sans-serif;font-weight:400;font-size:27px;color:var(--ink);margin-top:76px}
.card h3 b{font-weight:700}
.card p{font-size:13px;line-height:21px;margin:18px auto 0;width:360px;color:#3a3a4a}
.icon-badge{width:100px;height:100px;border-radius:50%;display:flex;align-items:center;justify-content:center;box-shadow:0 0 0 5px rgba(255,255,255,.9)}
.sheet-art{left:210px;top:2961px;width:275px;height:363px;border:2px solid #d0d0dc;border-radius:6px;background:linear-gradient(180deg,#2a2270 0 16%,#dfe8ee 16% 72%,#2a2270 72%)}
.sheet p{margin-top:30px;font-size:19px;line-height:26px;color:#3a3a4a}
.sheet .btn{margin-top:24px;width:246px;height:50px;border-radius:25px;font-size:13px;gap:6px}
.footer{top:3410px;left:0;width:1200px;height:212px;background:var(--ink-deep);color:var(--white)}
.footer .brand{position:absolute;left:145px;top:40px;color:var(--white);font-size:33px}
.footer .brand-mark{background:var(--white)}
.footer-links{position:absolute;left:476px;top:67px;display:flex;gap:44px;font-size:13px;text-transform:uppercase}
.footer .phone{position:absolute;left:940px;top:60px;color:var(--white);font-size:17px}
.footer-rule{position:absolute;left:142px;top:125px;width:992px;height:1px;background:rgba(255,255,255,.2)}
.copyright{position:absolute;left:156px;top:158px;font-size:11px}
.social{position:absolute;left:1018px;top:153px;display:flex;gap:6px}
.social span{width:25px;height:25px;border-radius:50%;background:var(--white);display:block}
</style>
</head>
<body>

<header class="abs nav">
  <div class="brand"><span class="brand-mark"></span>QuillRests</div>
  <nav class="nav-links"><span class="current">How it Works</span><span>Resources</span><span>Contact</span></nav>
  <div class="phone"><span class="phone-dot"><svg width="14" height="14" viewBox="0 0 24 24"><path fill="#fff" d="M6.6 10.8a15 15 0 0 0 6.6 6.6l2.2-2.2a1 1 0 0 1 1-.25 11.4 11.4 0 0 0 3.6.57 1 1 0 0 1 1 1V20a1 1 0 0 1-1 1A17 17 0 0 1 3 4a1 1 0 0 1 1-1h3.5a1 1 0 0 1 1 1c0 1.25.2 2.45.57 3.57a1 1 0 0 1-.25 1z"/></svg></span>555-014-2270</div>
</header>

<section class="abs hero">
  <div class="abs hero-copy">
    <p class="kicker">Welcome to QuillRests</p>
    <h1>Enhanced Protection<br>Against Airborne<br>Infectious Particles</h1>
  </div>
  <a class="btn">LEARN MORE</a>
  <div class="abs hero-video" role="img" aria-label="Video still: a doctor beside a patient resting in a hospital bed"></div>
  <div class="abs play" style="top:266px"></div>
  <svg class="abs" style="left:852px;top:285px" width="22" height="28" viewBox="0 0 22 28"><path d="M2 2 L20 14 L2 26Z" fill="#fff"/></svg>
</section>
<svg class="abs hero-curve" viewBox="0 0 1200 80" preserveAspectRatio="none">
  <path d="M0 75 Q600 -20 1200 75 L1200 80 L0 80Z" fill="#fff"/>
  <path d="M170 48 Q600 -8 1040 48" fill="none" stroke="#f1582c" stroke-width="5"/>
</svg>

<div class="abs dots-deco" role="img" aria-label="Decorative dot pattern"></div>

<div class="abs center" style="top:793px"><p class="eyebrow">Why We Are</p></div>
<div class="abs center" style="top:815px"><h2 class="section-title" style="font-size:39px">About <b>QuillRests</b></h2></div>
<div class="abs rule" style="left:572px;top:868px"></div>
<div class="abs about-body">
  <p>The QuillRest is an air filtration system that reduces the exposure to airborne infectious particles for healthcare workers, patients, and visitors by utilizing a source-focused technology that captures airborne infectious particles at the source.</p>
  <p>The QuillRest utilizes a patent-pending headboard design that pulls air from the head area of the patient through a HEPA filtration system and exhausts filtered air back into the room.</p>
</div>
<svg class="abs" style="left:589px;top:1103px" width="38" height="22" viewBox="0 0 38 22"><path d="M1 1 L19 20 L37 1" fill="none" stroke="#2a1d6b" stroke-width="2"/></svg>

<section class="abs band">
  <div class="abs band-art" role="img" aria-label="Diagram of three scenes showing airborne particles around a patient bed being captured at the source"></div>
</section>
<div class="abs band-copy">
  <h2>Source-Focused<br><b>HEPA Filtration</b></h2>
  <p>Capture airborne infectious<br>particles at the source</p>
</div>

<div class="abs n95-art" role="img" aria-label="White QuillRests air filtration unit on wheels"></div>
<div class="abs split-copy n95" style="top:1908px">
  <h2>Greater Protection<br><b>than an N95 Mask*</b></h2>
  <p>According to the NHA Study, "Expedient Methods for Surge Airborne Isolation within Healthcare Settings during Response to a Natural or Manmade Epidemic", the expedient airborne isolation research discussed within this document has identified isolation configurations that rely upon inexpensive, off-the-shelf materials and HEPA filtration systems that are commonly found within healthcare facilities. Most provide better real-time source protection from infectious aerosol than that expected to result from an N95 respirator. In several cases, the protection is several times better. &nbsp;*based on standard source focused air filtration cited in above named study available on our resources page.</p>
</div>

<section class="abs features"></section>
<div class="abs card" style="left:136px">
  <h3>Deploys in <b>Minutes</b></h3>
  <p>The QuillRest is a complete system that can be deployed in a matter of minutes using only basic tools. The system easily disassembles for sanitation.</p>
</div>
<div class="abs card" style="left:613px">
  <h3 style="margin-top:84px">9 <b>Minutes</b></h3>
  <p style="font-size:15px">Turns over air in a 15 x 20 room in 9 minutes.</p>
</div>
<div class="abs icon-badge" style="left:307px;top:2462px;background:var(--band)">
  <svg width="52" height="52" viewBox="0 0 52 52" fill="none" stroke="#fff" stroke-width="2"><circle cx="28" cy="29" r="15"/><circle cx="28" cy="29" r="10"/><path d="M28 22v7l5 3M25 10h6M28 10v4M6 24h8M4 30h8M7 36h8"/></svg>
</div>
<div class="abs icon-badge" style="left:785px;top:2462px;background:var(--orange)">
  <svg width="52" height="52" viewBox="0 0 52 52" fill="none" stroke="#fff" stroke-width="2"><path d="M12 30a16 16 0 1 1 8 14"/><path d="M28 14v14h10"/><text x="6" y="40" fill="#fff" stroke="none" font-family="DM Sans,sans-serif" font-size="13" font-weight="700">09'</text></svg>
</div>

<div class="abs sheet-art" role="img" aria-label="Cover of the QuillRests PDF quick info sheet showing a hospital room with the filtration unit"></div>
<div class="abs split-copy sheet" style="left:601px;top:3030px">
  <h2>QuillRests PDF<br><b>Quick Info Sheet</b></h2>
  <div class="rule" style="margin-top:12px"></div>
  <p>Quick download for a printable information piece on the QuillRests system.</p>
  <a class="btn"><svg width="14" height="14" viewBox="0 0 24 24" fill="none" stroke="#fff" stroke-width="2"><path d="M12 3v13M6 11l6 6 6-6M4 21h16"/></svg>DOWNLOAD QUICK SHEET</a>
</div>

<footer class="abs footer">
  <div class="brand"><span class="brand-mark"></span>QuillRests</div>
  <nav class="footer-links"><span>Home</span><span>How it works</span><span>Resources</span><span>Contact</span></nav>
  <div class="phone"><span class="phone-dot" style="width:32px;height:32px"><svg width="15" height="15" viewBox="0 0 24 24"><path fill="#fff" d="M6.6 10.8a15 15 0 0 0 6.6 6.6l2.2-2.2a1 1 0 0 1 1-.25 11.4 11.4 0 0 0 3.6.57 1 1 0 0 1 1 1V20a1 1 0 0 1-1 1A17 17 0 0 1 3 4a1 1 0 0 1 1-1h3.5a1 1 0 0 1 1 1c0 1.25.2 2.45.57 3.57a1 1 0 0 1-.25 1z"/></svg></span>555-014-2270</div>
  <div class="footer-rule"></div>
  <p class="copyright">©2022 by QuillRests LLC. All Right Reserved</p>
  <div class="social" aria-label="Social links"><span></span><span></span><span></span></div>
</footer>

</body>
</html>
```